Redesign the content on our home page

Thanks for your designs thus far.

There have been a few requests for feedback, so I have mocked up another layout. I am happy with everything except the 6 boxes in the green square. This is the piece I need the perfect design for.
- What the boxes look like
- Icons to be used
- Colours
- etc

__________________________________________________________________

We have the basic layout for our homepage, the header and footer are done. Please see attached (Homepage)

Only design in PSD etc needed, no coding. Also, header and footer not needed either, only formatting and graphic design of home page content. See eps file for the information.

I need more information added to the homepage and displayed in an organised way and designed so it presents well.

Our slogan is "Travel Insurance made simple". Therefore the design needs to represent this by being a simple, clear and clean layout of information. Website visitors need to be able to access and digest the information fast and this is reliant on the design of the information.

Attached is a mock up with all of the information.

Please ask and questions you need to help with the design.

Project Deadline Extended Reason: Deadline has been extended to provide further clarification for the required design.I need the 6 boxes inside the green outline designed. The design of the 6 boxes should be simple and follow the pages design and be simple in appearance. Thanks for your designs thus far. Added Thursday, October 8, 2015

Target Market(s)

Mostly female, any age.

Industry/Entity Type

Travel

Number of Pages Required

1 page

Font styles to use
Other font styles liked:
• MetaPro

Colors
f37122
33a6d7
33b8a4
dbdbdb
606060

Requirements
Must have
• - Follow home page look and feel
• - Simple design
• - Fast for a visitor to digest the information
Nice to have
• Simple design. Webpage is responsive so elements should look good when scaled for mobile.
Should not have
• No new colours to be introduced then what is in the design already or selected below.
• No new fonts.

```html
<!DOCTYPE html>
<html lang="en">
<head>
<meta charset="utf-8">
<title>Easyroam – Travel Insurance made simple</title>
<link href="https://fonts.googleapis.com/css2?family=Fira+Sans:wght@400;500;700&display=swap" rel="stylesheet">
<style>
:root{
  --orange:#f37122;
  --blue:#33a6d7;
  --teal:#33b8a4;
  --grey:#dbdbdb;
  --grey-light:#f2f2f2;
  --text:#606060;
  --white:#ffffff;
}
*{box-sizing:border-box;margin:0;padding:0}
html,body{width:1200px;height:3060px;overflow:hidden}
body{font-family:"Fira Sans",Arial,sans-serif;color:var(--text);background:var(--white);position:relative}
.abs{position:absolute}

/* header */
.site-header{left:0;top:0;width:1200px;height:60px;background:var(--white)}
.brand-name{font-weight:700;color:var(--orange);line-height:1}
.header-brand{left:80px;top:14px;font-size:32px}
.header-phone{right:80px;top:8px;font-size:16px;font-weight:700;color:var(--orange)}
.main-nav{right:80px;top:34px;display:flex;gap:22px;font-size:13px;color:var(--text)}

/* hero */
.hero{left:0;top:60px;width:1200px;height:380px;background:var(--orange);overflow:hidden}
.hero-art{left:90px;top:40px;width:300px;height:290px;border-radius:6px;background:linear-gradient(180deg,#f58a48,#e8651a)}
.hero-wave{left:0;bottom:0}

/* intro */
.page-title{left:0;top:470px;width:1200px;text-align:center;font-size:34px;font-weight:500;color:var(--orange)}
.intro{left:300px;top:526px;width:600px;text-align:center;font-size:14px;line-height:1.5}

/* features */
.features{left:170px;top:600px;width:860px;display:grid;grid-template-columns:repeat(3,1fr);column-gap:40px;row-gap:60px}
.feature{text-align:center}
.feature-icon{width:60px;height:60px;margin:0 auto 14px;background:var(--orange);border-radius:6px;display:flex;align-items:center;justify-content:center}
.feature-title{font-size:15px;font-weight:700;color:var(--orange);margin-bottom:10px;line-height:1.3}
.feature-text{font-size:12px;line-height:1.55}

/* award */
.award{left:140px;top:1130px;width:920px;height:240px;background:var(--orange)}
.award-badge{left:320px;top:70px;width:110px;height:56px;border-radius:8px;background:#8cc63f}
.award-copy{left:320px;top:140px;color:var(--white);font-size:12px;line-height:1.5}
.award-copy strong{font-size:13px}

/* confidence */
.confidence-title{left:0;top:1420px;width:1200px;text-align:center;font-size:26px;font-weight:500;color:var(--orange)}
.confidence-text{left:250px;top:1464px;width:700px;text-align:center;font-size:13px;line-height:1.5}
.confidence-lead{left:0;top:1518px;width:1200px;text-align:center;font-size:13px}
.cover-cards{left:140px;top:1556px;width:920px;display:grid;grid-template-columns:repeat(4,1fr);gap:24px}
.cover-card{position:relative;height:210px;border:2px solid var(--grey);padding:86px 18px 0;text-align:center;font-size:12px;line-height:1.55}
.cover-badge{position:absolute;left:50%;top:18px;transform:translateX(-50%);width:58px;height:58px}
.badge-square{background:var(--blue);border-radius:6px}
.badge-tag{background:var(--teal);border-radius:50%}
.badge-globe{background:#f6a46d;border-radius:50%}

/* rating */
.rating{left:140px;top:1830px;width:920px;height:46px;background:var(--orange);color:var(--white);font-size:14px;font-weight:500;text-align:center;line-height:46px}

/* resources */
.resources{left:0;top:1920px;width:1200px;height:190px;background:var(--grey-light)}
.resource-cards{left:200px;top:30px;width:800px;display:grid;grid-template-columns:repeat(3,1fr);gap:30px}
.resource-card{background:var(--white);height:130px;padding:20px 18px}
.resource-head{display:flex;align-items:center;gap:10px;font-size:17px;font-weight:700;color:var(--orange);margin-bottom:10px}
.resource-dot{width:30px;height:30px;border-radius:50%;background:var(--orange);flex:none}
.resource-text{font-size:12px;line-height:1.5}

/* skyline + press */
.skyline{left:0;top:2110px;width:1200px;height:340px;background:linear-gradient(180deg,#ffffff 0%,#ececec 70%,#e2e2e2 100%)}
.press-title{left:0;top:2462px;width:1200px;text-align:center;font-size:22px;color:var(--text)}
.press-row{left:220px;top:2506px;width:760px;display:flex;justify-content:space-between}
.press-logo{width:100px;height:40px;background:var(--grey);border-radius:4px}

/* footer */
.site-footer{left:0;top:2590px;width:1200px;height:360px;background:var(--orange)}
.footer-brand{left:70px;top:40px;width:270px;height:260px;background:var(--white);padding:30px 24px}
.footer-brand .brand-name{font-size:34px}
.footer-contact{margin-top:14px;font-size:14px;font-weight:700;color:var(--orange);line-height:1.5}
.footer-under{margin-top:26px;font-size:12px;color:var(--text)}
.footer-under strong{display:block;font-size:17px;color:var(--blue);margin-top:2px}
.footer-cols{left:380px;top:40px;width:760px;display:grid;grid-template-columns:repeat(3,1fr);gap:30px;color:var(--white)}
.footer-col h3{font-size:17px;font-weight:700;padding-bottom:10px;border-bottom:1px solid rgba(255,255,255,.5);margin-bottom:14px}
.footer-col p{font-size:14px;line-height:1.6}
.footer-col .gap{margin-top:16px}
.fine-print{left:60px;top:2966px;width:1080px;font-size:10px;line-height:1.6;color:var(--text)}
</style>
</head>
<body>

<header class="site-header abs">
  <div class="brand-name header-brand abs">easyroam</div>
  <div class="header-phone abs">1300 555 018</div>
  <nav class="main-nav abs">
    <span>Travel Insurance</span><span>Before you travel</span><span>Your Policy</span><span>FAQs</span><span>Emergency</span>
  </nav>
</header>

<section class="hero abs">
  <div class="hero-art abs" role="img" aria-label="Illustration of a traveller with a suitcase in front of a faint city skyline"></div>
  <svg class="hero-wave abs" width="1200" height="70" viewBox="0 0 1200 70">
    <path d="M0 70 L0 45 Q60 20 120 40 Q180 10 250 38 Q320 15 400 42 Q480 18 560 40 Q640 12 720 40 Q800 18 880 42 Q960 15 1040 38 Q1120 20 1200 42 L1200 70 Z" fill="#ffffff"/>
  </svg>
</section>

<h1 class="page-title abs">Travel Insurance made simple</h1>
<p class="intro abs">We tried figuring out why buying travel insurance was complicated, but we couldn't, so we made it simple.</p>

<section class="features abs">
  <div class="feature">
    <div class="feature-icon"><svg width="30" height="30" viewBox="0 0 30 30"><path d="M6 15 L12 21 L24 9" stroke="#fff" stroke-width="3.5" fill="none" stroke-linecap="round" stroke-linejoin="round"/></svg></div>
    <div class="feature-title">Get A Simple<br>Instant Quote</div>
    <p class="feature-text">Get your quote in seconds with only a few details about your trip. No forms to wade through, just a clear price shown straight away so you can decide fast.</p>
  </div>
  <div class="feature">
    <div class="feature-icon"><svg width="30" height="30" viewBox="0 0 30 30"><path d="M15 5 V25 M5 15 H25" stroke="#fff" stroke-width="4" stroke-linecap="round"/></svg></div>
    <div class="feature-title">No Medical<br>Assessments</div>
    <p class="feature-text">No lengthy medical checks for listed existing conditions. If your condition is on our list you are covered automatically, with nothing extra to fill in.</p>
  </div>
  <div class="feature">
    <div class="feature-icon"><svg width="30" height="30" viewBox="0 0 30 30"><rect x="8" y="5" width="14" height="20" rx="2" stroke="#fff" stroke-width="3" fill="none"/><path d="M12 12 H18 M12 17 H18" stroke="#fff" stroke-width="2.5"/></svg></div>
    <div class="feature-title">A Lower PDS<br>Word Count</div>
    <p class="feature-text">We wrote our policy wording in plain language and kept it short, so you can read it in one sitting and know exactly what you are covered for.</p>
  </div>
  <div class="feature">
    <div class="feature-icon"><svg width="30" height="30" viewBox="0 0 30 30"><path d="M6 15 H22 M16 9 L22 15 L16 21" stroke="#fff" stroke-width="3.5" fill="none" stroke-linecap="round" stroke-linejoin="round"/></svg></div>
    <div class="feature-title">Quick &amp; Simple<br>Purchase</div>
    <p class="feature-text">Buy online in a few easy steps. Your policy and certificate arrive by email within minutes, ready to print or keep on your phone for your trip.</p>
  </div>
  <div class="feature">
    <div class="feature-icon"><svg width="30" height="30" viewBox="0 0 30 30"><path d="M9 6 L13 6 L15 11 L12 13 Q14 18 18 19 L20 16 L25 18 L25 22 Q24 25 20 24 Q8 21 6 10 Q6 6 9 6 Z" fill="#fff"/></svg></div>
    <div class="feature-title">Fast Help<br>When You Need It</div>
    <p class="feature-text">When you need us most, help is one call away with our team available around the clock, wherever in the world your travels happen to take you.</p>
  </div>
  <div class="feature">
    <div class="feature-icon"><svg width="30" height="30" viewBox="0 0 30 30"><rect x="5" y="8" width="20" height="15" rx="2" stroke="#fff" stroke-width="3" fill="none"/><path d="M11 8 V6 H19 V8" stroke="#fff" stroke-width="3" fill="none"/></svg></div>
    <div class="feature-title">Simple<br>Online Claims</div>
    <p class="feature-text">Lodge a claim online in a few simple steps and track its progress any time. Upload your documents from home and get a quick, fair answer.</p>
  </div>
</section>

<section class="award abs">
  <div class="award-badge abs" role="img" aria-label="Ratewise award badge"></div>
  <div class="award-copy abs">
    <strong>Award Winning Travel Insurance</strong><br>
    Ratewise Experts Choice Award 2015<br>
    Best value comprehensive travel cover
  </div>
</section>

<h2 class="confidence-title abs">Travel with confidence</h2>
<p class="confidence-text abs">Wherever and whenever you are travelling, you need to spend your time enjoying your holiday instead of worrying about what you would do if something were to happen while you were away.</p>
<p class="confidence-lead abs">With Easyroam, you can travel confidently knowing you get cover:</p>

<section class="cover-cards abs">
  <div class="cover-card">
    <svg class="cover-badge" viewBox="0 0 58 58"><circle cx="29" cy="29" r="29" fill="#f37122"/><path d="M29 16 V42 M16 29 H42" stroke="#fff" stroke-width="7"/></svg>
    Unlimited overseas medical cover for emergency care, hospital stays and evacuation home.
  </div>
  <div class="cover-card">
    <div class="cover-badge badge-square" role="img" aria-label="Sentinel Underwriting partner badge"></div>
    Underwritten by Sentinel Underwriting, a trusted global insurer for many years.
  </div>
  <div class="cover-card">
    <div class="cover-badge badge-tag" role="img" aria-label="Round-the-clock assistance badge"></div>
    Emergency assistance team available 24 hours a day, 7 days a week, worldwide.
  </div>
  <div class="cover-card">
    <div class="cover-badge badge-globe" role="img" aria-label="Globe illustration"></div>
    Cover for cancellation, lost luggage and delays on trips all around the globe.
  </div>
</section>

<div class="rating abs">Easyroam Travel Insurance is rated 4.1 stars by 30 customers on ReviewHub as at 1/3/15</div>

<section class="resources abs">
  <div class="resource-cards abs">
    <div class="resource-card">
      <div class="resource-head"><span class="resource-dot"></span>Travel Alerts</div>
      <p class="resource-text">Latest safety warnings and news for the places you plan to visit.</p>
    </div>
    <div class="resource-card">
      <div class="resource-head"><span class="resource-dot"></span>Travel guides</div>
      <p class="resource-text">Handy tips and local know-how to help you plan the perfect trip.</p>
    </div>
    <div class="resource-card">
      <div class="resource-head"><span class="resource-dot"></span>Travel Blog</div>
      <p class="resource-text">Stories, ideas and inspiration from fellow travellers near and far.</p>
    </div>
  </div>
</section>

<div class="skyline abs" role="img" aria-label="Soft grey city skyline illustration"></div>
<h2 class="press-title abs">As seen on</h2>
<div class="press-row abs">
  <div class="press-logo" role="img" aria-label="Media outlet"></div>
  <div class="press-logo" role="img" aria-label="Media outlet"></div>
  <div class="press-logo" role="img" aria-label="Media outlet"></div>
  <div class="press-logo" role="img" aria-label="Media outlet"></div>
  <div class="press-logo" role="img" aria-label="Media outlet"></div>
  <div class="press-logo" role="img" aria-label="Media outlet"></div>
</div>

<footer class="site-footer abs">
  <div class="footer-brand abs">
    <div class="brand-name">easyroam</div>
    <div class="footer-contact">easyroam.example<br>1300 555 018</div>
    <div class="footer-under">Underwritten by<strong>Sentinel Underwriting</strong></div>
  </div>
  <div class="footer-cols abs">
    <div class="footer-col">
      <h3>Sales &amp; General Enquiries</h3>
      <p>1300 555 018<br>hello@easyroam.example<br>Fax (02) 5550 1234</p>
      <p class="gap">Easyroam Travel Insurance<br>PO Box 4410<br>Harbour Exchange NSW 1299</p>
    </div>
    <div class="footer-col">
      <h3>Claims</h3>
      <p>1300 555 019<br>claims@easyroam.example<br>Fax (07) 5550 8812</p>
      <p class="gap">Easyroam Travel Claims<br>PO Box 318<br>Riverbend QLD 4099</p>
    </div>
    <div class="footer-col">
      <h3>Administration</h3>
      <p>1300 555 018<br>admin@easyroam.example<br>Fax (02) 5550 1234</p>
      <p class="gap">Level 12, Market Tower,<br>88 Quay Street<br>Sydney NSW 2000</p>
    </div>
  </div>
</footer>

<p class="fine-print abs">Easyroam Pty Ltd ABN 00 000 000 000 arranges this insurance as an authorised representative of Sentinel Underwriting Ltd, which issues and manages the policy. Any advice on this site is general only and does not take into account your objectives, financial situation or needs. Please read the Product Disclosure Statement before deciding whether this insurance is right for you. We receive a commission that is a percentage of your premium; ask us for more information about this. Cover is subject to the terms, conditions, limits and exclusions set out in the policy wording, and is available to residents only.</p>

</body>
</html>
```